BRAMLEIGH real estate family office

Hello, Our business is a real estate intermediation activity on high-end goods (amounts exceeding € 10m) for corporate and private clients. You can see our logo on the site www.bramleigh-invented.fr We would like to keep that spirit with the hexagon that represents France (transactions between Monaco and Saint Tropez, Courchevel and Paris). And the "baseline" that is "real estate family office". The corporate logo should be and can be printed by embossing (relief). We must integrate the name, first name, phone, email and website. Finally, to imbibe the spirit of business, here is a detail of the activity. "Genuine consulting firm in real estate investments, BRAMLEIGH works with its customers as a specialized player in the high-end markets, we are recognized for our ultra-confidential approach and tailor-made, as well as the quality of our network. We broadcast any information on the market and we work exclusively through a strong relationship we have developed over the years. BRAMLEIGH is active on the French Riviera (from Monaco to Saint-Tropez), the Alps (Courchevel, Méribel, Megève) and Paris (essentially market premium). Always looking for opportunities for our clients, we work on two investment areas: residential luxury real estate (properties, vineyards, mansions, land, etc.) commercial real estate (empty office buildings or yield, hotel properties, land, etc.) "

Target Market(s)

High foreign end customers. corporate and private.

Industry/Entity Type

Real Estate

Contact Information for Business Card

LOGO
baseline
Laurent Dufossé
+33(0)6.41.57.09.64
ld@bramleigh-invented.fr
www.bramleigh-invented.fr

Font styles to use
Serif

Colors
cedeed
0255a3
3277b5
85abd2
85cae6
34a7d7
0792cd
cfdeed
1b1b1b

Requirements
Must have
• see description

```html
<!DOCTYPE html>
<html lang="en">
<head>
<meta charset="utf-8">
<title>BRAMLEIGH business card</title>
<link rel="stylesheet" href="https://fonts.googleapis.com/css2?family=Montserrat:wght@300;400;600&family=Tinos:wght@400;700&display=swap">
<style>
  :root {
    --bg: #2a2a2c;
    --card-top: #232325;
    --card-bottom: #050506;
    --ink-white: #f2f2f2;
    --ink-grey: #8c8c90;
    --rule-grey: #6d6d72;
    --brand-blue: #2f4fc0;
    --mark-grey: #3c3c40;
  }
  html, body {
    margin: 0;
    padding: 0;
    width: 1200px;
    height: 913px;
    overflow: hidden;
    background: var(--bg);
  }
  .canvas {
    position: relative;
    width: 1200px;
    height: 913px;
    display: flex;
    align-items: center;
    justify-content: center;
    gap: 60px;
  }
  .card {
    position: relative;
    width: 520px;
    height: 325px;
    border-radius: 16px;
    background: linear-gradient(160deg, var(--card-top) 0%, var(--card-bottom) 70%);
    box-shadow: 0 18px 40px rgba(0,0,0,0.55);
    overflow: hidden;
    font-family: "Montserrat", sans-serif;
    color: var(--ink-white);
  }
  /* front */
  .brand {
    position: absolute;
    left: 36px;
    top: 150px;
  }
  .brand-name {
    font-weight: 300;
    font-size: 34px;
    letter-spacing: 4px;
    line-height: 1;
    color: var(--ink-white);
  }
  .brand-baseline {
    margin: 6px 0 0 72px;
    font-weight: 300;
    font-size: 12px;
    letter-spacing: 0.5px;
    color: var(--ink-white);
  }
  .holder-name {
    position: absolute;
    right: 32px;
    top: 58px;
    font-family: "Tinos", serif;
    font-weight: 700;
    font-size: 18px;
    letter-spacing: 0.5px;
    text-transform: uppercase;
    color: var(--brand-blue);
  }
  .rule-top {
    position: absolute;
    right: 24px;
    top: 86px;
    width: 250px;
    height: 2px;
    background: var(--rule-grey);
  }
  .rule-bottom {
    position: absolute;
    left: 24px;
    top: 232px;
    width: 230px;
    height: 2px;
    background: var(--rule-grey);
  }
  .contacts {
    position: absolute;
    left: 34px;
    top: 244px;
    margin: 0;
    padding: 0;
    list-style: none;
    font-size: 12.5px;
    font-weight: 400;
    line-height: 21px;
  }
  .contacts li {
    display: flex;
    align-items: center;
    gap: 10px;
  }
  .contacts svg {
    width: 11px;
    height: 11px;
    flex: none;
  }
  .contacts strong { font-weight: 600; }
  .edge-band {
    position: absolute;
    right: 0;
    bottom: 0;
    width: 120px;
    height: 6px;
    background: var(--brand-blue);
  }
  /* back */
  .back-name {
    position: absolute;
    left: 0;
    right: 0;
    top: 120px;
    text-align: center;
    font-weight: 300;
    font-size: 44px;
    letter-spacing: 8px;
    color: var(--mark-grey);
  }
  .back-web {
    position: absolute;
    right: 36px;
    bottom: 40px;
    font-size: 14px;
    font-weight: 400;
    color: var(--ink-white);
  }
  .back-web span {
    color: var(--brand-blue);
    font-weight: 600;
  }
</style>
</head>
<body>
<main class="canvas">
  <section class="card card-front">
    <div class="brand">
      <div class="brand-name">BRAMLEIGH</div>
      <div class="brand-baseline">real estate family office</div>
    </div>
    <div class="holder-name">Laurent Dufossé</div>
    <div class="rule-top"></div>
    <div class="rule-bottom"></div>
    <ul class="contacts">
      <li>
        <svg viewBox="0 0 12 12" aria-hidden="true"><path d="M2 1.5 L4 1 L5 3.5 L3.8 4.5 Q5 7 7.5 8.2 L8.5 7 L11 8 L10.5 10 Q5 10.5 1.5 3 Z" fill="var(--brand-blue)"/></svg>
        +33(0)6.41.57.09.64
      </li>
      <li>
        <svg viewBox="0 0 12 12" aria-hidden="true"><circle cx="6" cy="6" r="5" fill="none" stroke="var(--brand-blue)" stroke-width="1.5"/><circle cx="6" cy="6" r="2" fill="var(--brand-blue)"/></svg>
        ld@bramleigh-invented.fr
      </li>
      <li>
        <svg viewBox="0 0 12 12" aria-hidden="true"><circle cx="6" cy="6" r="5" fill="none" stroke="var(--brand-blue)" stroke-width="1.2"/><ellipse cx="6" cy="6" rx="2" ry="5" fill="none" stroke="var(--brand-blue)" stroke-width="1"/><line x1="1" y1="6" x2="11" y2="6" stroke="var(--brand-blue)" stroke-width="1"/></svg>
        www.<strong>bramleigh-invented</strong>.fr
      </li>
    </ul>
    <div class="edge-band"></div>
  </section>

  <section class="card card-back">
    <div class="back-name">BRAMLEIGH</div>
    <div class="back-web">www.<span>bramleigh-invented</span>.fr</div>
  </section>
</main>
</body>
</html>
```